Redesign of business card for Birchline Mechanical

We are looking for a new design for our business cards for Birchline Mechanical. We are a plumbing & HVAC construction company, operating on the West Coast of Canada and USA. Logo attached.
Industry/Entity Type
Construction - Plumbing & HVAC
Contact Information for Business Card
Name, address, phone numbers, email, website address
Look and feel
Each slider illustrates characteristics of the customer's brand and the style your logo design should communicate.

```html
<!DOCTYPE html>
<html lang="en">
<head>
<meta charset="utf-8">
<title>Birchline Mechanical – Business Card</title>
<link href="https://fonts.googleapis.com/css2?family=Oswald:wght@500&family=Montserrat:wght@400;700&family=Inter:wght@400&display=swap" rel="stylesheet">
<style>
  :root{
    --backdrop:#464646;
    --slate-top:#6b7480;
    --slate-bottom:#434c5e;
    --amber:#e8a427;
    --white:#ffffff;
    --ink:#111111;
    --text-grey:#4a4f5a;
    --rule:#5a5e66;
    --paper-top:#ffffff;
    --paper-bottom:#e9eaec;
  }
  *{margin:0;padding:0;box-sizing:border-box}
  html,body{width:1200px;height:1000px;overflow:hidden;background:var(--backdrop)}
  .card{position:absolute;left:291px;width:652px;height:404px;border-radius:14px;overflow:hidden}
  .card--front{top:81px;background:linear-gradient(160deg,var(--slate-top) 0%,var(--slate-bottom) 100%)}
  .card--back{top:530px;background:linear-gradient(160deg,var(--paper-top) 0%,#f3f3f4 55%,var(--paper-bottom) 100%)}

  .wordmark{position:absolute;display:flex;align-items:center;gap:12px;font-family:'Oswald',sans-serif;font-weight:500;text-transform:uppercase;letter-spacing:1px;white-space:nowrap}
  .wordmark__square{display:block;flex:none}
  .front-wordmark{left:0;right:0;top:104px;justify-content:center;color:var(--white);font-size:44px}
  .front-wordmark .wordmark__square{width:34px;height:34px;background:var(--white)}

  .services{position:absolute;left:0;top:0;width:652px;height:404px}
  .service-badge{position:absolute;width:54px;height:54px;border-radius:50%;background:var(--amber)}
  .service-label{position:absolute;top:296px;transform:translateX(-50%);font-family:'Montserrat',sans-serif;font-size:14px;letter-spacing:5px;color:#e4e7ec;white-space:nowrap}
  .service-divider{position:absolute;top:296px;width:1px;height:18px;background:#e4e7ec}

  .web-band{position:absolute;left:0;top:0}
  .web-address{position:absolute;left:0;right:0;top:343px;text-align:center;font-family:'Montserrat',sans-serif;font-size:14px;letter-spacing:4.5px;color:#2b2f38}

  .back-wordmark{left:58px;top:88px;color:var(--ink);font-size:26px;gap:9px}
  .back-wordmark .wordmark__square{width:20px;height:20px;background:var(--ink)}
  .faint-wordmark{right:-30px;top:44px;color:#ffffff;opacity:.75;font-size:64px}

  .company-name{position:absolute;left:59px;top:208px;font-family:'Montserrat',sans-serif;font-weight:700;font-size:16.5px;color:var(--ink);letter-spacing:.2px}
  .company-name span{color:var(--amber)}
  .name-rule{position:absolute;left:59px;top:235px;width:540px;height:1px;background:var(--rule)}
  .name-rule-accent{position:absolute;left:556px;top:234px;width:43px;height:3px;background:var(--amber)}

  .contact-list{position:absolute;left:58px;top:254px;list-style:none}
  .contact-list li{display:flex;align-items:center;height:25px;font-family:'Inter',sans-serif;font-size:14px;letter-spacing:1.6px;color:var(--text-grey)}
  .contact-list svg{width:16px;height:16px;margin-right:13px;flex:none}

  .address{position:absolute;right:57px;top:310px;text-align:right;font-family:'Inter',sans-serif;font-size:14px;line-height:19px;color:var(--text-grey)}
  .address-pin{position:absolute;left:578px;top:281px}
</style>
</head>
<body>

<section class="card card--front" aria-label="Business card front">
  <div class="wordmark front-wordmark"><span class="wordmark__square"></span>Birchline Mechanical</div>

  <div class="services">
    <div class="service-badge" style="left:167px;top:236px" role="img" aria-label="Construction icon"></div>
    <div class="service-badge" style="left:316px;top:236px" role="img" aria-label="HVAC unit icon"></div>
    <div class="service-badge" style="left:449px;top:236px" role="img" aria-label="Plumbing icon"></div>
    <span class="service-label" style="left:199px">CONSTRUCTION</span>
    <span class="service-divider" style="left:293px"></span>
    <span class="service-label" style="left:345px">HVAC</span>
    <span class="service-divider" style="left:403px"></span>
    <span class="service-label" style="left:473px">PLUMBING</span>
  </div>

  <svg class="web-band" width="652" height="404" viewBox="0 0 652 404" aria-hidden="true">
    <rect x="41" y="363" width="570" height="2.5" fill="var(--amber)"/>
    <path d="M216 365 L236 345 Q241 340 248 340 L438 340 Q445 340 450 345 L470 365 Z" fill="var(--amber)"/>
  </svg>
  <div class="web-address">www.birchlinemech.com</div>
</section>

<section class="card card--back" aria-label="Business card back">
  <div class="wordmark faint-wordmark">Birchline</div>
  <div class="wordmark back-wordmark"><span class="wordmark__square"></span>Birchline Mechanical</div>

  <h1 class="company-name">BIRCHLINE <span>MECHANICAL</span></h1>
  <div class="name-rule"></div>
  <div class="name-rule-accent"></div>

  <ul class="contact-list">
    <li>
      <svg viewBox="0 0 16 16" aria-hidden="true"><rect x="1" y="4" width="14" height="10" rx="1" fill="none" stroke="var(--amber)" stroke-width="1.6"/><path d="M1.5 5 L8 10 L14.5 5" fill="none" stroke="var(--amber)" stroke-width="1.6"/></svg>
      info@birchlinemech.com
    </li>
    <li>
      <svg viewBox="0 0 16 16" aria-hidden="true"><path d="M1 6 Q8 1 15 6 L13 8 L11 6.5 L5 6.5 L3 8 Z" fill="var(--amber)"/><rect x="3" y="8" width="10" height="6" rx="1.5" fill="var(--amber)"/></svg>
      1-866-555-0142
    </li>
    <li>
      <svg viewBox="0 0 16 16" aria-hidden="true"><circle cx="8" cy="8" r="7" fill="none" stroke="var(--amber)" stroke-width="1.4"/><path d="M5 4.5 L6.5 4.5 L7 6.5 L6 7.3 Q7 9.3 8.7 10 L9.5 9 L11.5 9.5 L11.5 11 Q7.5 11.5 5 7 Z" fill="var(--amber)"/></svg>
      213-555-0187
    </li>
    <li>
      <svg viewBox="0 0 16 16" aria-hidden="true"><circle cx="8" cy="8" r="7" fill="none" stroke="var(--amber)" stroke-width="1.4"/><path d="M1 8 H15 M8 1 Q4 8 8 15 M8 1 Q12 8 8 15" fill="none" stroke="var(--amber)" stroke-width="1.2"/></svg>
      www.birchlinemech.com
    </li>
  </ul>

  <svg class="address-pin" width="18" height="26" viewBox="0 0 18 26" aria-hidden="true">
    <path d="M9 1 C4.5 1 1 4.4 1 8.8 C1 14 9 21 9 21 C9 21 17 14 17 8.8 C17 4.4 13.5 1 9 1 Z" fill="var(--amber)"/>
    <circle cx="9" cy="8.8" r="2.6" fill="#ffffff"/>
    <rect x="4" y="23.5" width="10" height="1.6" fill="var(--amber)"/>
  </svg>
  <address class="address" style="font-style:normal">4120 Harbor Lane, Suite 200,<br>Costa Mesa, CA 92626</address>
</section>

</body>
</html>
```